upgrade old website to new wordpress website

Looking to have kwrmedbill.com upgraded to a new wordpress website utilizing much of the content already present. While still pairing down or presenting differently the current information. Clean design with no fast moving or difficult to navigate links or pages. Looking for blog type space for tips on billing issues found and work arounds for the issues. Want to update monthly or less. Link to show website of our software vendor available for some clients to demonstrate amount of software options available (www.vantorimed.com). Do not want anyone to Leave our site, just have access to see the other site. More captions or area of interest to describe specific types of providers we bill for. IE: ambulance, ambulette, Ems go together and we have experience in partnering and billing with Brek data & Medvo pad software amoung others. 40 Yr experience in Chiropractic billing especially Workers Comp and Auto. 96% collections for Certified Nurse Practitioners and Physical therapists. Rest of pages should explain our experience, another for our percentage of collection results for providers. Another for our credentialing experience and services. Another for our Management services. Some type of contact for more information that requests the type of provider they are and what they are looking for .

Target Market(s)

Client information and front face of company.

Coding

Coded - Design and coding required

Number of Pages Required

5+ page

Font styles to use
Sans Serif

Requirements
Must have
• Be compatible with tablets and regular computers. Ability to upload to my own webhost and information blocks that can be updated if needed in future. Wining page upgradable and fully functional.
Nice to have
• Small blog update section, blurbs for information, additional pages for more in depth information. Cleaner look to pages and theme.
Should not have
• Difficult to find pages or hidden information

```html
<!DOCTYPE html>
<html lang="en">
<head>
<meta charset="utf-8">
<title>KWR Health Services</title>
<link href="https://fonts.googleapis.com/css2?family=Roboto:wght@400;500&family=Roboto+Condensed:wght@400;500&display=swap" rel="stylesheet">
<style>
:root{
  --navy:#0f0e4d;
  --topbar:#262626;
  --footer:#1e1e1e;
  --footer-base:#141414;
  --panel:#dfe2ef;
  --band:#ececec;
  --ink:#1d1d1f;
  --body:#444;
  --muted:#8a8a8a;
  --accent:#c0392b;
  --white:#fff;
}
*{margin:0;padding:0;box-sizing:border-box}
html,body{width:798px;height:1200px;overflow:hidden;background:var(--white)}
body{position:relative;font-family:"Roboto",sans-serif;color:var(--body)}
.abs{position:absolute}

.topbar{left:0;top:0;width:798px;height:32px;background:var(--topbar);color:#ddd;font-size:8px}
.topbar .item{position:absolute;top:11px;display:flex;align-items:center;gap:5px}

.header{left:0;top:32px;width:798px;height:62px;background:var(--white)}
.brand{left:65px;top:18px;font-family:"Roboto Condensed",sans-serif;font-weight:500;font-size:16px;color:var(--navy);border-bottom:1.5px solid var(--navy);padding-bottom:2px}
.nav{left:281px;top:0;height:62px;display:flex}
.nav a{display:block;height:62px;line-height:62px;font-size:8px;color:#333;text-decoration:none;padding:0 15px;text-transform:uppercase}
.nav a.active{background:#dde0ea;color:var(--navy);border-bottom:3px solid var(--navy);line-height:60px}

.hero{left:0;top:94px;width:798px;height:383px;background:linear-gradient(120deg,#4a4d55 0%,#6e7480 30%,#9fb6d8 55%,#7f8c9f 80%,#5a606c 100%)}
.arrow{position:absolute;top:166px}
.caption{left:150px;top:225px;width:496px;height:123px;background:rgba(220,228,248,.55);text-align:center}
.caption h1{font-family:"Roboto Condensed",sans-serif;font-weight:400;font-size:22px;color:var(--ink);margin-top:16px;letter-spacing:.3px}
.caption p{font-size:13px;color:var(--ink);margin-top:4px}
.btn{display:inline-block;margin-top:8px;width:88px;height:32px;line-height:32px;background:var(--navy);color:var(--white);font-size:9px;text-transform:uppercase;letter-spacing:.3px}

.feature{top:501px;width:205px;height:190px;background:var(--panel);text-align:center}
.feature .icon{width:64px;height:64px;border-radius:50%;background:var(--navy);margin:20px auto 0;border:2px solid #fff;display:flex;align-items:center;justify-content:center}
.feature h3{font-family:"Roboto Condensed",sans-serif;font-weight:500;font-size:12px;color:var(--ink);margin-top:15px;letter-spacing:.3px}
.feature p{font-size:7.4px;line-height:17px;color:#555;margin:8px 15px 0}

.section-title{font-family:"Roboto Condensed",sans-serif;font-weight:500;font-size:19px;color:var(--ink);letter-spacing:.3px;white-space:nowrap}
.welcome{left:74px;top:718px;width:318px}
.welcome p{font-size:8px;line-height:17.1px;color:#444;margin-top:6px}
.why{left:429px;top:718px;width:300px}
.why ul{list-style:none;margin-top:6px}
.why li{font-size:7.6px;line-height:20.5px;color:#333;display:flex;align-items:center;gap:3px}
.why li .note{color:var(--accent);margin-left:6px}

.partners{left:0;top:887px;width:798px;height:74px;background:var(--band)}
.partners .row{position:absolute;left:77px;top:29px;width:640px;display:flex;justify-content:space-between;align-items:center}
.partners .rule{position:absolute;left:74px;bottom:0;width:650px;height:2px;background:var(--navy)}
.partner{font-family:"Roboto",sans-serif;font-weight:500;font-size:10px;color:#9a9a9a;letter-spacing:.4px;white-space:nowrap;display:flex;align-items:center;gap:4px}
.partner .dot{width:8px;height:8px;background:#a8a8a8;border-radius:50%}

.footer{left:0;top:961px;width:798px;height:187px;background:var(--footer);color:#bbb}
.footer h4{position:absolute;top:22px;font-family:"Roboto Condensed",sans-serif;font-weight:500;font-size:11px;color:#fff;letter-spacing:.3px}
.news{position:absolute;left:74px;width:205px}
.news .thumb{position:absolute;left:0;top:0;width:62px;height:48px;background:linear-gradient(135deg,#c9d3de,#8ea2b8);border-bottom:2px solid var(--navy)}
.news .txt{position:absolute;left:67px;top:0;width:138px}
.news .t{font-size:7.6px;color:#eee;line-height:10.5px}
.news .d{font-size:7.2px;color:#888;line-height:12px;margin-top:2px}
.news-sep{position:absolute;left:74px;width:205px;height:1px;background:#333}
.contact{position:absolute;left:309px;top:44px;font-size:7.4px;color:#ccc}
.contact .row{position:absolute;left:0;display:flex;gap:7px;white-space:nowrap;line-height:13.5px}
.contact .sub{color:#aaa}
.socials{position:absolute;left:309px;top:146px;display:flex;gap:4px}
.socials span{width:13px;height:13px;border-radius:50%;background:#5a6a8a}
.testimonial{position:absolute;left:520px;top:44px;width:204px}
.avatar{position:absolute;left:0;top:0;width:39px;height:36px;background:linear-gradient(160deg,#6d7b8e,#2f3847);border-bottom:2px solid var(--navy)}
.testimonial .name{position:absolute;left:47px;top:3px;font-size:8px;color:#fff}
.testimonial .co{position:absolute;left:47px;top:18px;font-size:7px;color:#777}
.testimonial .rule{position:absolute;left:0;top:44px;width:204px;height:1px;background:#333}
.testimonial .quote{position:absolute;left:0;top:55px;font-size:7.2px;line-height:15px;color:#999}
.pager{position:absolute;left:700px;top:25px;display:flex;gap:4px}
.pager span{width:9px;height:9px;border-radius:50%;background:#2a2a2a}

.base{left:0;top:1148px;width:798px;height:52px;background:var(--footer-base);font-size:7.6px;color:#666}
.base .links{position:absolute;left:74px;top:22px}
.base .copy{position:absolute;right:74px;top:22px}
</style>
</head>
<body>

<div class="abs topbar">
  <div class="item" style="left:553px">
    <svg width="10" height="8" viewBox="0 0 10 8"><rect width="10" height="8" rx="1" fill="#ddd"/><path d="M0 1l5 3.5L10 1" stroke="#262626" fill="none"/></svg>
    info@kwrmedbill.com
  </div>
  <div class="item" style="left:656px">
    <svg width="8" height="8" viewBox="0 0 8 8"><path d="M1 0.5l2 0 0.8 2-1 0.8a5 5 0 0 0 2 2l0.8-1 2 0.8 0 2c-4 0.5-7-2.5-6.6-6.6z" fill="#ddd"/></svg>
    (555)-210-4473
  </div>
</div>

<header class="abs header">
  <div class="abs brand">K.W.R. Health Services</div>
  <nav class="abs nav">
    <a class="active" href="#">Home</a>
    <a href="#">Billing Services</a>
    <a href="#">Management Services</a>
    <a href="#">About Us</a>
    <a href="#">Links</a>
    <a href="#">Contact</a>
  </nav>
</header>

<section class="abs hero" role="img" aria-label="Photo of two businessmen shaking hands in front of office towers">
  <svg class="arrow" style="left:12px" width="22" height="40" viewBox="0 0 22 40"><path d="M20 1L2 20l18 19" stroke="#fff" stroke-width="1.2" fill="none"/></svg>
  <svg class="arrow" style="left:764px" width="22" height="40" viewBox="0 0 22 40"><path d="M2 1l18 19L2 39" stroke="#fff" stroke-width="1.2" fill="none"/></svg>
  <div class="abs caption">
    <h1>KWR HEALTH SERVICES</h1>
    <p>Defining Great Practices</p>
    <span class="btn">Read More</span>
  </div>
</section>

<div class="abs feature" style="left:74px">
  <div class="icon"><svg width="24" height="20" viewBox="0 0 24 20" fill="#fff"><circle cx="6" cy="5" r="3"/><circle cx="18" cy="5" r="3"/><circle cx="12" cy="7" r="3.5"/><path d="M1 15c0-4 10-4 10 0zM13 15c0-4 10-4 10 0zM5 19c0-6 14-6 14 0z"/></svg></div>
  <h3>FAMILY OWNED</h3>
  <p>Ut wisi enim ad minim veniam, quis nostrud exerci tation ullamcorper suscipit lobortis nisl ut aliquip ex ea commodo consequat.</p>
</div>
<div class="abs feature" style="left:297px">
  <div class="icon"><svg width="20" height="20" viewBox="0 0 20 20" fill="#fff"><rect x="2" y="9" width="4" height="9"/><path d="M7 9l4-7c2 0 2 2 1.5 4H17c1.5 0 2 1.5 1.5 2.5l-2 8c-.3 1-1 1.5-2 1.5H7z"/></svg></div>
  <h3>PUBLICLY DEDICATED</h3>
  <p>Lorem ipsum dolor sit amet, consectetuer adipiscing elit, sed diam nonummy nibh euismod tincidunt ut laoreet dolore magna aliquam erat volutpat.</p>
</div>
<div class="abs feature" style="left:519px">
  <div class="icon"><svg width="22" height="20" viewBox="0 0 22 20" fill="#fff"><path d="M6 1h10v6a5 5 0 0 1-10 0z"/><path d="M6 3H2c0 4 2 6 4.5 6M16 3h4c0 4-2 6-4.5 6" stroke="#fff" stroke-width="1.5" fill="none"/><rect x="10" y="12" width="2" height="4"/><rect x="6.5" y="16" width="9" height="3"/></svg></div>
  <h3>NATIONALLY ACCREDITED</h3>
  <p>Ut wisi enim ad minim veniam, quis nostrud exerci tation ullamcorper suscipit lobortis nisl ut aliquip ex ea commodo consequat.</p>
</div>

<section class="abs welcome">
  <h2 class="section-title">WELCOME TO KWR HEALTH SERVICES</h2>
  <p>Lorem ipsum dolor sit amet, consectetuer adipiscing elit, sed diam nonummy nibh eui smod tincidunt ut laoreet dolore magna aliquam erat volutpat. Ut wisi enim ad minim veniam, quis nostrud exerci tation ullamcorper suscipit lobortis nisl ut aliquip ex ea commodo consequat. Duis autem vel eum iriure dolor in hendrerit in vulputate velit esse molestie consequat, vel illum dolore eu feugiat nulla facilisis at vero eros et accumsan et iusto odio dignissim qui blandit praesent luptatum zzril delenit augue duis dolore te feugait nulla facilisi.</p>
</section>

<section class="abs why">
  <h2 class="section-title">WHY CHOOSE US</h2>
  <ul>
    <li><svg width="8" height="8" viewBox="0 0 8 8"><circle cx="4" cy="4" r="4" fill="var(--navy)"/><path d="M2 4h3.5M4 2.3L5.7 4 4 5.7" stroke="#fff" stroke-width="1" fill="none"/></svg>Meeting All your medical billing needs for over 30 years.</li>
    <li><svg width="8" height="8" viewBox="0 0 8 8"><circle cx="4" cy="4" r="4" fill="var(--navy)"/><path d="M2 4h3.5M4 2.3L5.7 4 4 5.7" stroke="#fff" stroke-width="1" fill="none"/></svg>Collection Rates + 90% <span class="note">Can your current billing company say that?</span></li>
    <li><svg width="8" height="8" viewBox="0 0 8 8"><circle cx="4" cy="4" r="4" fill="var(--navy)"/><path d="M2 4h3.5M4 2.3L5.7 4 4 5.7" stroke="#fff" stroke-width="1" fill="none"/></svg>HIPAA Compliant</li>
    <li><svg width="8" height="8" viewBox="0 0 8 8"><circle cx="4" cy="4" r="4" fill="var(--navy)"/><path d="M2 4h3.5M4 2.3L5.7 4 4 5.7" stroke="#fff" stroke-width="1" fill="none"/></svg>View your patient accounts in real time.</li>
    <li><svg width="8" height="8" viewBox="0 0 8 8"><circle cx="4" cy="4" r="4" fill="var(--navy)"/><path d="M2 4h3.5M4 2.3L5.7 4 4 5.7" stroke="#fff" stroke-width="1" fill="none"/></svg>No minimum monthly fees.</li>
    <li><svg width="8" height="8" viewBox="0 0 8 8"><circle cx="4" cy="4" r="4" fill="var(--navy)"/><path d="M2 4h3.5M4 2.3L5.7 4 4 5.7" stroke="#fff" stroke-width="1" fill="none"/></svg>We can custom tailor our services to meet your needs.</li>
  </ul>
</section>

<section class="abs partners" aria-label="Partner names">
  <div class="row">
    <div class="partner">Northvale</div>
    <div class="partner"><span class="dot"></span>Brightpath</div>
    <div class="partner">Corlane</div>
    <div class="partner"><span class="dot"></span>Meridex</div>
    <div class="partner">Tallow</div>
    <div class="partner">Fenwick</div>
    <div class="partner">Cardin</div>
  </div>
  <div class="rule"></div>
</section>

<footer class="abs footer">
  <h4 style="left:74px">RECENT NEWS</h4>
  <div class="news" style="top:44px">
    <div class="thumb" role="img" aria-label="Photo of office staff at a desk"></div>
    <div class="txt"><div class="t">Lorem ipsum dolor sit amet, cons ectetuer</div><div class="d">Ut wisi enim ad minim veniam, quis nostrud exerci tation ulla mcorper...</div></div>
  </div>
  <div class="news-sep" style="top:105px"></div>
  <div class="news" style="top:118px">
    <div class="thumb" role="img" aria-label="Photo of a team meeting around a laptop"></div>
    <div class="txt"><div class="t">Ut wisi enim ad minim veniam, quis nostrud exerci tation ullamcorper</div><div class="d">Eodem modo typi, qui nunc nobis videntur parum clari, fiant sollemnes...</div></div>
  </div>

  <h4 style="left:309px">CONTACT US</h4>
  <div class="contact">
    <div class="row" style="top:0">
      <svg width="7" height="9" viewBox="0 0 7 9"><path d="M3.5 0a3.5 3.5 0 0 1 3.5 3.5C7 6 3.5 9 3.5 9S0 6 0 3.5A3.5 3.5 0 0 1 3.5 0z" fill="#ccc"/><circle cx="3.5" cy="3.5" r="1.3" fill="#1e1e1e"/></svg>
      <div>KWR HEALTH<br><span class="sub">48 Harbor Point Dr, Suite B<br>Ridgefield, Ohio. 43990</span></div>
    </div>
    <div class="row" style="top:43px"><svg width="10" height="8" viewBox="0 0 10 8"><rect width="10" height="8" rx="1" fill="#ccc"/><path d="M0 1l5 3.5L10 1" stroke="#1e1e1e" fill="none"/></svg>info@kwrmedbill.com</div>
    <div class="row" style="top:67px"><svg width="9" height="9" viewBox="0 0 9 9"><rect width="9" height="9" rx="1.5" fill="#ccc"/><path d="M2.5 2l1.2 0 .5 1.3-.6.5a3 3 0 0 0 1.3 1.3l.5-.6 1.3.5 0 1.2C4.5 6.6 2.3 4.5 2.5 2z" fill="#1e1e1e"/></svg><div>(555)-210-4473<br>(555)-210-4472</div></div>
  </div>
  <div class="socials" aria-label="Social links"><span></span><span></span><span></span><span></span><span></span><span></span></div>

  <h4 style="left:520px">TESTMONIALS</h4>
  <div class="pager"><span></span><span></span></div>
  <div class="testimonial">
    <div class="avatar" role="img" aria-label="Portrait photo of a client in a suit"></div>
    <div class="name">Mark Ellison</div>
    <div class="co">Company Name</div>
    <div class="rule"></div>
    <div class="quote">" Lorem ipsum dolor sit amet consectetur adipisci ng elit. Sed commodo dui id sem vehicula rhoncus. Aenean posuere purus vel enim sodales tincidunt. rhoncus. Aenean posuere purus vel enim.</div>
  </div>
</footer>

<div class="abs base">
  <div class="links">Privacy Policy &nbsp;|&nbsp; Sitemap</div>
  <div class="copy">Copyrights@2015 KWR Health.. All Right Reserved.</div>
</div>

</body>
</html>
```